Luminar Kidneywise Banner for BKT Conference

We need banners for our upcoming conference. I have attached the design we have started, but we are not graphic designers and don't have the eye to know what needs to be fixed. We want one banner to have our 3 products (Primed for Wards, Steady at Surgery, and TOOLvantage) and the other banner to have the overall goal of the company. The dimensions of the banner are 33x81, but the recommend not getting too close to the edge. The descriptions for each product must be included under each product. We do not want the banners to be too busy and we don't want many images other than the logo.

Target Market(s)

Physicians/ Medical Practice Managers

Colors
0054AA
0677BA
7BADD7
CADEEF
E8F1F8
00AB8E
00BBA5
67D7C9
C6EFE9
E9F9F6

Requirements
Must have
• Company Colors, social media logos for instagram,linkedin, and facebook
Nice to have
• Unique touches, Logo on both banners

```html
<!DOCTYPE html>
<html lang="en">
<head>
<meta charset="utf-8">
<title>Luminar Kidneywise – Conference Banners</title>
<link rel="stylesheet" href="https://fonts.googleapis.com/css2?family=Montserrat:wght@400;500;600;800;900&display=swap">
<style>
  :root{
    --stage:#e3e5f8;
    --paper:#eef3f6;
    --blue-deep:#0054aa;
    --blue:#0677ba;
    --blue-soft:#7badd7;
    --blue-pale:#cadeef;
    --teal-deep:#00ab8e;
    --teal:#00bba5;
    --teal-soft:#67d7c9;
    --teal-pale:#c6eff9;
    --ink-grey:#6d6e71;
    --rule:#c9cccd;
    --white:#ffffff;
  }
  *{box-sizing:border-box;margin:0;padding:0}
  html,body{width:1200px;height:1200px;overflow:hidden;background:var(--stage);font-family:"Montserrat",sans-serif}
  .banner{position:absolute;top:154px;width:364px;height:902px;background:var(--paper);overflow:hidden;box-shadow:0 6px 18px rgba(60,60,90,.18)}
  .banner--products{left:230px}
  .banner--mission{left:646px}
  .wave{position:absolute;left:0;width:364px}
  .wave--top{top:0;height:130px}
  .wave--bottom{bottom:0;height:110px}

  .seal{position:absolute;left:60px;top:84px;width:248px;height:248px;border-radius:50%;background:var(--white);border:6px solid var(--teal);box-shadow:0 10px 18px rgba(0,0,0,.14);display:flex;align-items:center;justify-content:center;text-align:center}
  .seal__name{font-weight:800;font-size:24px;line-height:1.15;color:var(--blue)}

  .product__title{position:absolute;left:0;width:302px;height:44px;border-radius:0 22px 22px 0;background:linear-gradient(90deg,var(--blue),var(--blue-deep));color:var(--white);font-weight:900;font-size:18px;letter-spacing:.2px;line-height:44px;padding-left:13px}
  .product__title::after{content:"";position:absolute;right:15px;top:16px;width:12px;height:12px;border-radius:50%;background:var(--white)}
  .product__desc{position:absolute;left:13px;width:338px;height:65px;border-radius:32px 0 0 32px;background:linear-gradient(90deg,var(--teal),var(--teal-deep));color:var(--white);font-weight:500;font-size:12.4px;line-height:15.5px;padding:17px 20px 0 19px}
  .rule{position:absolute;left:110px;width:143px;height:1.5px;background:var(--rule)}

  .social{position:absolute;left:0;width:364px;top:782px;text-align:center}
  .social__handle{font-size:9px;color:var(--ink-grey);font-weight:500}
  .social__icons{margin-top:5px;display:flex;justify-content:center;gap:9px}
  .social__icon{width:27px;height:27px;border-radius:5px;background:var(--ink-grey)}

  .brand-card{position:absolute;left:23px;top:118px;width:323px;height:180px;background:var(--white);border:4px solid var(--blue);border-radius:58px 12px 58px 0;box-shadow:0 8px 16px rgba(0,0,0,.12);display:flex;align-items:center;justify-content:center;text-align:center}
  .brand-card__name{font-weight:800;font-size:30px;line-height:1.1;color:var(--ink-grey)}

  .pillar{position:absolute;left:16px;width:326px;height:63px;border-radius:32px;background:linear-gradient(90deg,var(--blue),var(--blue-deep));display:flex;align-items:center;padding-left:10px}
  .pillar__check{width:44px;height:44px;border-radius:50%;background:var(--white);display:flex;align-items:center;justify-content:center;flex:none}
  .pillar__label{margin-left:12px;color:var(--white);font-weight:900;font-size:29px;letter-spacing:.3px}
</style>
</head>
<body>

<section class="banner banner--products">
  <svg class="wave wave--top" viewBox="0 0 364 130" preserveAspectRatio="none" aria-hidden="true">
    <defs>
      <linearGradient id="blueSweep" x1="0" y1="0" x2="0" y2="1">
        <stop offset="0" stop-color="#0054aa"/><stop offset="1" stop-color="#0677ba"/>
      </linearGradient>
    </defs>
    <path d="M0 0H364V110C300 70 230 50 170 58C100 66 45 90 0 112Z" fill="url(#blueSweep)"/>
    <path d="M0 70C70 40 150 28 220 34C280 40 330 58 364 78" fill="none" stroke="#7badd7" stroke-width="5" opacity=".9"/>
    <path d="M0 84C80 58 170 48 250 56C300 62 340 76 364 92" fill="none" stroke="#cadeef" stroke-width="2" opacity=".8"/>
  </svg>

  <div class="seal"><span class="seal__name">Luminar<br>Kidneywise</span></div>

  <h2 class="product__title" style="top:351px">TOOLVANTAGE</h2>
  <p class="product__desc" style="top:407px">Monthly webinars to help integrate APP’s into your nephrology practice.</p>
  <div class="rule" style="top:482px"></div>

  <h2 class="product__title" style="top:492px">PRIMED FOR WARDS</h2>
  <p class="product__desc" style="top:546px">Train APP’s ready to safely round in dialysis units in 8 weeks.</p>
  <div class="rule" style="top:622px"></div>

  <h2 class="product__title" style="top:636px">STEADY AT SURGERY</h2>
  <p class="product__desc" style="top:690px">Educate APPs to deliver sound Nephrology care in the office in 3 weeks.</p>
  <div class="rule" style="top:770px"></div>

  <div class="social">
    <p class="social__handle">LuminarKidneywise</p>
    <div class="social__icons"><span class="social__icon"></span><span class="social__icon"></span><span class="social__icon"></span></div>
  </div>

  <svg class="wave wave--bottom" viewBox="0 0 364 110" preserveAspectRatio="none" aria-hidden="true">
    <defs>
      <linearGradient id="tealSweepUp" x1="0" y1="1" x2="0" y2="0">
        <stop offset="0" stop-color="#00ab8e"/><stop offset="1" stop-color="#00bba5"/>
      </linearGradient>
    </defs>
    <path d="M0 110H364V20C300 50 230 64 170 58C100 52 45 34 0 24Z" fill="url(#tealSweepUp)"/>
    <path d="M0 60C80 80 170 86 250 76C300 70 340 56 364 44" fill="none" stroke="#67d7c9" stroke-width="5" opacity=".9"/>
    <path d="M0 46C80 66 170 72 250 64C300 58 340 46 364 34" fill="none" stroke="#c6efe9" stroke-width="2" opacity=".8"/>
  </svg>
</section>

<section class="banner banner--mission">
  <svg class="wave wave--top" viewBox="0 0 364 130" preserveAspectRatio="none" aria-hidden="true">
    <defs>
      <linearGradient id="tealSweep" x1="0" y1="0" x2="0" y2="1">
        <stop offset="0" stop-color="#00ab8e"/><stop offset="1" stop-color="#00bba5"/>
      </linearGradient>
    </defs>
    <path d="M0 0H364V110C300 70 230 50 170 58C100 66 45 90 0 112Z" fill="url(#tealSweep)"/>
    <path d="M0 70C70 40 150 28 220 34C280 40 330 58 364 78" fill="none" stroke="#67d7c9" stroke-width="5" opacity=".9"/>
    <path d="M0 84C80 58 170 48 250 56C300 62 340 76 364 92" fill="none" stroke="#c6efe9" stroke-width="2" opacity=".8"/>
  </svg>

  <div class="brand-card"><span class="brand-card__name">Luminar<br>Kidneywise</span></div>

  <div class="pillar" style="top:354px"><span class="pillar__check"><svg width="26" height="22" viewBox="0 0 26 22"><path d="M3 11l7 7L23 4" fill="none" stroke="#00ab8e" stroke-width="5" stroke-linecap="round" stroke-linejoin="round"/></svg></span><span class="pillar__label">TRAIN</span></div>
  <div class="rule" style="top:436px"></div>
  <div class="pillar" style="top:459px"><span class="pillar__check"><svg width="26" height="22" viewBox="0 0 26 22"><path d="M3 11l7 7L23 4" fill="none" stroke="#00ab8e" stroke-width="5" stroke-linecap="round" stroke-linejoin="round"/></svg></span><span class="pillar__label">EDUCATE</span></div>
  <div class="rule" style="top:542px"></div>
  <div class="pillar" style="top:564px"><span class="pillar__check"><svg width="26" height="22" viewBox="0 0 26 22"><path d="M3 11l7 7L23 4" fill="none" stroke="#00ab8e" stroke-width="5" stroke-linecap="round" stroke-linejoin="round"/></svg></span><span class="pillar__label">INTEGRATE</span></div>
  <div class="rule" style="top:648px"></div>
  <div class="pillar" style="top:670px"><span class="pillar__check"><svg width="26" height="22" viewBox="0 0 26 22"><path d="M3 11l7 7L23 4" fill="none" stroke="#00ab8e" stroke-width="5" stroke-linecap="round" stroke-linejoin="round"/></svg></span><span class="pillar__label">MANAGE</span></div>
  <div class="rule" style="top:748px"></div>

  <div class="social">
    <p class="social__handle">LuminarKidneywise</p>
    <div class="social__icons"><span class="social__icon"></span><span class="social__icon"></span><span class="social__icon"></span></div>
  </div>

  <svg class="wave wave--bottom" viewBox="0 0 364 110" preserveAspectRatio="none" aria-hidden="true">
    <defs>
      <linearGradient id="blueSweepUp" x1="0" y1="1" x2="0" y2="0">
        <stop offset="0" stop-color="#0054aa"/><stop offset="1" stop-color="#0677ba"/>
      </linearGradient>
    </defs>
    <path d="M0 110H364V20C300 50 230 64 170 58C100 52 45 34 0 24Z" fill="url(#blueSweepUp)"/>
    <path d="M0 60C80 80 170 86 250 76C300 70 340 56 364 44" fill="none" stroke="#7badd7" stroke-width="5" opacity=".9"/>
    <path d="M0 46C80 66 170 72 250 64C300 58 340 46 364 34" fill="none" stroke="#cadeef" stroke-width="2" opacity=".8"/>
  </svg>
</section>

</body>
</html>
```